Dietary supplement package design

We need a design for a range of dietary supplements mentioned below. The colors can be derived from the attached company logo and the package is a plastic bottle for medicines use (attached is a sample). All products will have the same package design and color with a permissible slight change to product name and associated picture/artwork (if any). Please avoid using pictures of humans or animals. We expect to see a label with three panels:
1. Left panel containing instructions, warnings and other information.
2. Front panel containing products name and its unique look
3. Right panel containing nutrient/ingredient information table and address.
The label will dual language (Arabic/English) and we have no issue to use special colors, i.e. UV, gold or silver.
Products names are:
1. Ginkgo biloba
2. Slimming formula
3. Fat Absorber
4. Glutathione
5. Royal Jelly
6. Vitamin D
Consumers and health care professionals
Healthcare

```html
<!DOCTYPE html>
<html lang="en">
<head>
<meta charset="utf-8">
<title>Glutathione Supplement Label</title>
<link href="https://fonts.googleapis.com/css2?family=Fredoka:wght@600&family=Roboto+Condensed:wght@400;700&family=Archivo+Black&family=Tajawal:wght@400;500&display=swap" rel="stylesheet">
<style>
  :root {
    --bg: #e4e6e9;
    --label-top: #f4f5f7;
    --label-shade: #dcdfe3;
    --brand-blue: #1b73c2;
    --pill-blue: #8cc0ec;
    --ink: #1d1d1f;
    --white: #ffffff;
    --logo-blue: #1a82d0;
  }
  * { box-sizing: border-box; margin: 0; padding: 0; }
  html, body { width: 1200px; height: 675px; overflow: hidden; }
  body {
    background: var(--bg);
    font-family: "Roboto Condensed", sans-serif;
    color: var(--ink);
  }
  .label {
    position: absolute; left: 30px; top: 98px;
    width: 1140px; height: 480px;
    display: flex; gap: 18px;
  }
  .panel {
    position: relative; flex: 1; overflow: hidden;
    background: linear-gradient(180deg, var(--label-top) 0%, var(--label-shade) 100%);
  }
  .band {
    position: absolute; left: 0; right: 0; bottom: 0; height: 235px;
    background: var(--brand-blue);
  }
  /* Left panel */
  .directions { position: absolute; left: 26px; right: 26px; top: 36px; font-size: 15px; line-height: 1.45; }
  .directions b { font-weight: 700; }
  .disclaimer { margin-top: 14px; font-style: italic; font-size: 17px; line-height: 1.25; }
  .arabic {
    font-family: "Tajawal", sans-serif; direction: rtl; text-align: right;
    color: var(--white); font-size: 17px; line-height: 1.6;
  }
  .directions-ar { position: absolute; left: 26px; right: 26px; bottom: 34px; }
  /* Front panel */
  .front-wave { position: absolute; left: 0; bottom: 0; width: 100%; height: 330px; }
  .brand {
    position: absolute; top: 44px; left: 0; right: 0; text-align: center;
    font-family: "Fredoka", sans-serif; font-weight: 600; font-size: 30px; color: var(--logo-blue);
  }
  .brand-dot {
    display: block; width: 34px; height: 34px; margin: 0 auto 4px;
    border-radius: 50%; background: var(--logo-blue);
  }
  .emblem {
    position: absolute; left: 50%; top: 128px; width: 118px; height: 118px;
    margin-left: -59px; border-radius: 50%;
    background: radial-gradient(circle, #ffffff 0%, #cfe2f5 60%, #8fb9e3 100%);
  }
  .product-name {
    position: absolute; top: 282px; left: 0; right: 0; text-align: center;
    font-family: "Archivo Black", sans-serif; font-size: 40px; font-weight: 400; color: var(--white);
    letter-spacing: -0.5px;
  }
  .product-name-ar {
    position: absolute; top: 334px; left: 0; right: 0; text-align: center;
    font-family: "Tajawal", sans-serif; font-size: 24px; color: var(--white);
  }
  .count {
    position: absolute; top: 392px; padding: 5px 16px; border-radius: 18px;
    background: var(--pill-blue); color: var(--white); font-size: 20px;
  }
  .count-en { left: 34px; }
  .count-ar { right: 34px; font-family: "Tajawal", sans-serif; direction: rtl; }
  /* Right panel */
  .nutrition {
    position: absolute; left: 78px; top: 24px; width: 226px;
    background: var(--white); border: 2px solid var(--ink); padding: 6px 8px;
    font-size: 10px; line-height: 1.35; z-index: 2;
  }
  .nutrition h2 { font-family: "Archivo Black", sans-serif; font-size: 22px; font-weight: 400; line-height: 1.1; }
  .nutrition .rule-thick { border-top: 6px solid var(--ink); margin: 3px 0; }
  .nutrition .row { display: flex; justify-content: space-between; border-top: 1px solid var(--ink); }
  .nutrition .sub { padding-left: 10px; }
  .nutrition .note { font-size: 9px; }
  .producer {
    position: absolute; left: 0; right: 0; bottom: 50px; text-align: center;
    color: var(--white); font-size: 15px; line-height: 1.4;
  }
  .producer strong { font-size: 16px; }
</style>
</head>
<body>
  <main class="label">
    <section class="panel panel-left">
      <div class="directions">
        <p><b>Usage:</b> Take 1 capsule once a day after a meal.</p>
        <p><b>How to store:</b> Keep in a cool, dry place and away from sunlight.</p>
        <p><b>Warning:</b> Not recommended for children or pregnant women.</p>
        <p class="disclaimer">This product is not intended to diagnose, treat, cure or prevent any disease.</p>
      </div>
      <div class="band"></div>
      <div class="arabic directions-ar">
        <p>لا يقصد من هذا المنتج تشخيص المرض</p>
        <p>طريقة الاستخدام: خذ 1 كبسولة واحدة في اليوم بعد وجبة الطعام.</p>
        <p>طريقة التخزين: يحفظ في مكان بارد وجاف وبعيدا عن أشعة الشمس.</p>
        <p>تحذير: لا ينصح به للأطفال أو النساء الحوامل.</p>
      </div>
    </section>

    <section class="panel panel-front">
      <svg class="front-wave" viewBox="0 0 368 330" preserveAspectRatio="none" aria-hidden="true">
        <path d="M0 20 C60 10 90 20 110 50 C140 130 228 130 258 50 C278 20 308 10 368 20 L368 330 L0 330 Z" fill="#1b73c2"/>
      </svg>
      <div class="brand"><span class="brand-dot"></span>Orvanelle</div>
      <div class="emblem" role="img" aria-label="Circular rosette emblem in blue line art"></div>
      <h1 class="product-name">Glutathione</h1>
      <p class="product-name-ar">الجلوتاثيون</p>
      <span class="count count-en">30 tablets</span>
      <span class="count count-ar">30 أقراص</span>
    </section>

    <section class="panel panel-right">
      <div class="band"></div>
      <div class="nutrition">
        <h2>Nutrition Facts</h2>
        <p>Serving Size 375 g</p>
        <div class="rule-thick"></div>
        <p><b>Amount Per Serving</b></p>
        <div class="row"><span><b>Calories</b> 345</span><span>Calories from Fat 138</span></div>
        <div class="row"><span></span><span>% Daily Value*</span></div>
        <div class="row"><span><b>Total Fat</b> 22.0g</span><span>34%</span></div>
        <div class="row sub"><span>Saturated Fat 10.2g</span><span>51%</span></div>
        <div class="row"><span><b>Cholesterol</b> 70mg</span><span>23%</span></div>
        <div class="row"><span><b>Sodium</b> 486mg</span><span>20%</span></div>
        <div class="row"><span><b>Total Carbohydrates</b> 11.2g</span><span>4%</span></div>
        <div class="row sub"><span>Dietary Fiber 4.2g</span><span>17%</span></div>
        <div class="row sub"><span>Sugars 5.8g</span><span></span></div>
        <div class="row"><span><b>Protein</b> 22.2g</span><span></span></div>
        <div class="rule-thick"></div>
        <div class="row"><span>Vitamin A 39%</span><span>Vitamin C 43%</span></div>
        <div class="row"><span>Calcium 4%</span><span>Iron 15%</span></div>
        <div class="row"><span><b>Nutrition Grade C</b></span><span></span></div>
        <p class="note">* Based on a 2000 calorie diet</p>
      </div>
      <div class="producer">
        <strong>Produced By:</strong><br>
        xxx Pharmaceutical Manufacturing<br>
        address: xx,xxxx,xxxx,
      </div>
    </section>
  </main>
</body>
</html>
```